Business Card Design

I need a business card design. I am a sole practitioner.I am a psychotherapist and I need a professional card. I am also an art therapist (a form of psychotherapy using art) so I want the image to be professional/creative/maybe ethnic. I do not want a boring minimalist "medical" image, nor do I want it too hippy/tree hugging.
Colours like reds/ochres/yellows would be good.
Contact Information for Business Card
Mira Hask
Psychotherapy, Counselling and Art Therapy
Wunnara Lodge Counselling and Wellbeing services
17 Pellow Road, Kelmarsh 4071
0417639052 www.MiraHask.com.au
on rear of card I need the option to have at least 4 or 5 appointment times /dates

```html
<!DOCTYPE html>
<html lang="en">
<head>
<meta charset="utf-8">
<title>Mira Hask – Business Card</title>
<link rel="stylesheet" href="https://fonts.googleapis.com/css2?family=Cinzel:wght@400&family=Open+Sans:wght@400&display=swap">
<style>
  :root {
    --page: #e9e4dc;
    --card: #2b2622;
    --bronze: #b8864e;
    --slot: #ffffff;
  }
  * { box-sizing: border-box; margin: 0; padding: 0; }
  html, body { width: 1200px; height: 989px; overflow: hidden; }
  body {
    background: var(--page);
    display: flex; flex-direction: column; align-items: center; justify-content: center;
    gap: 60px;
    font-family: "Open Sans", Arial, sans-serif;
    color: var(--bronze);
  }
  h1, h2, h3 { font-weight: 400; }
  .card {
    position: relative;
    width: 720px; height: 414px;
    background: var(--card);
    border-radius: 4px;
    box-shadow: 0 6px 18px rgba(0,0,0,.25);
  }
  .brand { display: flex; align-items: center; gap: 26px; }
  .brand-mark { width: 120px; height: 120px; background: var(--bronze); flex: none; }
  .brand-name {
    font-family: "Cinzel", Georgia, serif;
    font-size: 58px; letter-spacing: 4px; line-height: 1;
  }
  .brand-tagline { font-size: 17px; margin-top: 8px; }

  /* front */
  .card-front .brand { position: absolute; left: 56px; top: 52px; }
  .contact-list {
    position: absolute; left: 56px; bottom: 50px;
    list-style: none; font-size: 16px; line-height: 1.75;
  }
  .contact-list li { display: flex; align-items: center; gap: 10px; }
  .contact-list svg { width: 14px; height: 14px; fill: var(--bronze); flex: none; }
  .address {
    position: absolute; right: 56px; bottom: 50px;
    font-size: 16px; line-height: 1.75; text-align: right;
  }

  /* back */
  .card-back .brand { position: absolute; left: 50px; top: 44px; gap: 16px; }
  .card-back .brand-mark { width: 64px; height: 64px; }
  .card-back .brand-name { font-size: 36px; letter-spacing: 2px; }
  .card-back .brand-tagline { font-size: 11px; margin-top: 4px; }
  .appointment-title {
    position: absolute; left: 50px; top: 140px;
    font-family: "Cinzel", Georgia, serif; font-size: 24px; letter-spacing: 3px;
  }
  .appointment-rows {
    position: absolute; left: 50px; right: 50px; top: 196px;
    display: grid; grid-template-columns: auto 1fr auto 1fr;
    column-gap: 14px; row-gap: 16px; align-items: center;
    font-family: "Cinzel", Georgia, serif; font-size: 17px;
  }
  .slot { height: 30px; background: var(--slot); }
</style>
</head>
<body>
  <section class="card card-front" aria-label="Card front">
    <div class="brand">
      <div class="brand-mark"></div>
      <div>
        <h1 class="brand-name">MIRA HASK</h1>
        <p class="brand-tagline">Psychotherapy, Counselling and Art Therapy</p>
      </div>
    </div>
    <ul class="contact-list">
      <li><svg viewBox="0 0 24 24" aria-hidden="true"><path d="M6.6 10.8a15.1 15.1 0 0 0 6.6 6.6l2.2-2.2a1 1 0 0 1 1-.25 11.4 11.4 0 0 0 3.6.57 1 1 0 0 1 1 1V20a1 1 0 0 1-1 1A17 17 0 0 1 3 4a1 1 0 0 1 1-1h3.5a1 1 0 0 1 1 1c0 1.25.2 2.45.57 3.57a1 1 0 0 1-.25 1z"/></svg>0417639052</li>
      <li><svg viewBox="0 0 24 24" aria-hidden="true"><path d="M2 5h20v14H2zm2 2v.5l8 5 8-5V7l-8 5z"/></svg>hello@mirahask.com.au</li>
      <li><svg viewBox="0 0 24 24" aria-hidden="true"><path d="M12 2a10 10 0 1 0 0 20 10 10 0 0 0 0-20zm0 2c1.2 1.4 2 3.6 2.2 7H9.8c.2-3.4 1-5.6 2.2-7zM4.1 13h3.7c.1 2.4.6 4.4 1.4 5.9A8 8 0 0 1 4.1 13zm0-2a8 8 0 0 1 5.1-5.9C8.4 6.6 7.9 8.6 7.8 11zm5.7 2h4.4c-.2 3.4-1 5.6-2.2 7-1.2-1.4-2-3.6-2.2-7zm6.4 0h3.7a8 8 0 0 1-5.1 5.9c.8-1.5 1.3-3.5 1.4-5.9zm0-2c-.1-2.4-.6-4.4-1.4-5.9a8 8 0 0 1 5.1 5.9z"/></svg>www.MiraHask.com.au</li>
    </ul>
    <p class="address">Wunnara Lodge Counselling<br>and Wellbeing services<br>17 Pellow Road, Kelmarsh 4071</p>
  </section>

  <section class="card card-back" aria-label="Card back">
    <div class="brand">
      <div class="brand-mark"></div>
      <div>
        <h2 class="brand-name">MIRA HASK</h2>
        <p class="brand-tagline">Psychotherapy, Counselling and Art Therapy</p>
      </div>
    </div>
    <h3 class="appointment-title">APPOINTMENT</h3>
    <div class="appointment-rows">
      <span>Date:</span><span class="slot"></span><span>Time:</span><span class="slot"></span>
      <span>Date:</span><span class="slot"></span><span>Time:</span><span class="slot"></span>
      <span>Date:</span><span class="slot"></span><span>Time:</span><span class="slot"></span>
      <span>Date:</span><span class="slot"></span><span>Time:</span><span class="slot"></span>
    </div>
  </section>
</body>
</html>
```